Zerovan Medical

We are a medical supplier company we sell machines and equipment to all medical sectors in Iraq. Our services include not only the installation of these machines and equipment but also we provide support after installation and we train the staff to use these machines/equipment
We need a website that will make us stand out from our competitors, something professional and catchy
Starting from the home page, before showing the home page we want the loading screen to have our logo animated in a nice way
Then we can proceed to creating the other pages which are
Projects
Services
Training
About
and Contact us
Attached below is our logo and the color blue that we hope to use in the theme of the website
**** In the home page we want to focus on our partners and services****

Target Market(s)

Medical Sector

Industry/Entity Type

Medical

Coding

Coded - Design and coding required

Number of Pages Required

5+ page

Colors
0054AA
0677BA
7BADD7
CADEEF
E8F1F8

Requirements
Must have
• Animation in loading screen or animation in home page
Nice to have
• Some sort of animation for our partners

```html
<!DOCTYPE html>
<html lang="en">
<head>
<meta charset="utf-8">
<title>Zerovan Medical</title>
<link href="https://fonts.googleapis.com/css2?family=Poppins:wght@400;500;600;700&display=swap" rel="stylesheet">
<style>
:root{
  --navy:#1f2062;
  --navy-deep:#17184a;
  --blue:#0677BA;
  --blue-bright:#1b8fd8;
  --blue-dark:#0054AA;
  --sky:#7BADD7;
  --pale:#CADEEF;
  --mist:#E8F1F8;
  --grey-band:#f3f4f6;
  --text:#1c1c1c;
  --muted:#555;
  --line:#d5d7dc;
  --star:#f5a623;
}
*{box-sizing:border-box;margin:0;padding:0}
html,body{width:1200px;height:4812px;overflow:hidden;background:#fff}
body{position:relative;font-family:'Poppins',sans-serif;color:var(--text)}
.abs{position:absolute}
.ph{position:absolute}
.btn{position:absolute;display:flex;align-items:center;justify-content:center;font-weight:600;font-size:11px;color:#fff;background:var(--blue-bright);letter-spacing:.3px;text-transform:uppercase}
.btn.navy{background:var(--navy)}
.section-title{position:absolute;left:0;width:1200px;text-align:center;font-weight:700;font-size:30px;color:var(--text)}

/* top bar */
.topbar{left:0;top:0;width:1200px;height:30px;background:var(--navy);color:#fff;font-size:10.5px}
.topbar span{position:absolute;top:8px;display:flex;align-items:center;gap:6px}
.topbar svg{width:11px;height:11px}

/* nav */
.nav{left:0;top:30px;width:1200px;height:56px;background:#fff}
.brand{position:absolute;display:flex;align-items:center;gap:8px;font-weight:700;color:var(--blue-dark)}
.brand i{display:block;width:30px;height:30px;border:3px solid var(--blue-bright)}
.nav .links{position:absolute;left:402px;top:18px;display:flex;gap:34px;font-size:13px;color:#333}
.nav .links .on{color:var(--blue-bright)}
.icon-round{position:absolute;top:14px;width:24px;height:24px;border:1.5px solid #333;border-radius:50%}
.lang{position:absolute;left:1028px;top:12px;width:50px;height:28px;border:1.5px solid var(--navy);font-size:12px;padding:5px 8px}

/* hero */
.hero{left:0;top:86px;width:1200px;height:523px;
  background:
    radial-gradient(ellipse 180px 260px at 570px 290px,rgba(225,235,242,.75),rgba(225,235,242,0) 100%),
    radial-gradient(ellipse 300px 220px at 860px 260px,rgba(90,170,225,.55),rgba(90,170,225,0) 100%),
    linear-gradient(100deg,#1f3f57 0%,#3d6985 35%,#6f9cb8 65%,#9cc1d6 100%)}
.hero-text{left:122px;top:236px;color:#fff}
.hero-text .welcome{font-size:18px;font-weight:500}
.hero-text h1{font-size:40px;font-weight:700;margin-top:4px;line-height:1.15}
.hero-text p{font-size:18px;font-weight:600;line-height:1.25;margin-top:8px;width:370px}

/* quote */
.quote{left:243px;top:490px;width:712px;height:164px;background:#fff;box-shadow:0 2px 10px rgba(0,0,0,.08)}
.quote-tab{left:471px;top:490px;width:249px;height:30px;background:var(--navy);color:#fff;font-weight:600;font-size:16px;text-align:center;line-height:30px}
.field{position:absolute;background:#f2f3f5;font-size:11px;color:#333;padding:8px 10px}

/* services */
.svc{position:absolute;top:781px;width:305px;height:271px;background:#fff;border:1.5px solid var(--line);box-shadow:4px 4px 0 var(--navy)}
.svc .ico{position:absolute;left:18px;top:20px;width:74px;height:74px}
.svc h3{position:absolute;left:16px;top:104px;font-size:15px;font-weight:600}
.svc p{position:absolute;left:16px;top:128px;width:270px;font-size:11.5px;line-height:1.6;color:var(--muted)}
.svc a{position:absolute;left:16px;top:234px;font-size:11px;font-weight:600;color:var(--navy);text-decoration:underline}

/* category */
.cat-label{position:absolute;font-weight:600;color:var(--navy)}
.outline-btn{position:absolute;border:1.5px solid var(--navy);font-size:11px;font-weight:600;color:var(--navy);display:flex;align-items:center;justify-content:center}

/* products */
.band{left:3px;top:1734px;width:1197px;height:808px;background:var(--grey-band)}
.prod{position:absolute;width:309px;height:313px;background:#fff;border:1.5px solid #c9ccd2}
.prod .img{position:absolute;left:6px;top:6px;width:294px;height:182px}
.prod h4{position:absolute;left:0;width:100%;top:196px;text-align:center;font-size:16px;font-weight:600;line-height:1.3}
.prod .price{position:absolute;left:60px;top:258px;width:88px;height:30px;border:1.5px solid #333;font-size:12px;font-weight:600;display:flex;align-items:center;justify-content:center}
.prod .buy{position:absolute;left:157px;top:258px;width:88px;height:30px;background:var(--navy);color:#fff;font-size:10px;font-weight:600;display:flex;align-items:center;justify-content:center}

/* about */
.about h2{position:absolute;left:690px;top:2643px;font-size:30px;font-weight:700}
.about p{position:absolute;left:690px;top:2690px;width:360px;font-size:11.5px;line-height:1.7;color:var(--muted)}

/* reviews */
.rev{position:absolute;top:3073px;width:307px;height:273px;background:#fff;border:1.5px solid var(--line)}
.rev .top{position:absolute;left:0;top:0;width:100%;height:175px;background:var(--navy);color:#fff}
.rev .q{position:absolute;left:14px;top:10px;font-size:54px;font-weight:700;color:#5a5c9a;line-height:1}
.rev .top p{position:absolute;left:26px;top:54px;width:255px;text-align:center;font-size:11.5px;line-height:1.6}
.rev .avatar{position:absolute;left:123px;top:146px;width:60px;height:60px;border-radius:50%;background:#fff;border:3px solid #fff}
.rev .avatar i{position:absolute;inset:3px;border-radius:50%;background:#8a96a8}
.rev h5{position:absolute;left:0;width:100%;top:214px;text-align:center;font-size:14px;font-weight:600}
.rev .stars{position:absolute;left:0;width:100%;top:234px;text-align:center;color:var(--star);font-size:13px;letter-spacing:3px}
.arrow{position:absolute;top:3198px;width:22px;height:22px;border-radius:50%;background:var(--sky);color:#fff;font-size:12px;text-align:center;line-height:22px}

/* training */
.train{left:0;top:3398px;width:1200px;height:422px;
  background:
    radial-gradient(ellipse 200px 200px at 760px 170px,rgba(120,190,230,.7),rgba(120,190,230,0) 100%),
    linear-gradient(90deg,#cfe3f4 0%,#c3dcf0 38%,#6fa6d0 58%,#2f76ad 75%,#8fa9bd 100%)}
.play{position:absolute;left:120px;top:3646px;width:58px;height:58px;border-radius:50%;background:#fff;border:4px solid var(--blue-bright)}
.watch{position:absolute;left:188px;top:3664px;font-size:12px;font-weight:600;color:var(--blue-bright)}

/* blog */
.blog{position:absolute;top:3923px;width:308px;height:325px;background:#fff;border:1.5px solid #c9ccd2}
.blog .img{position:absolute;left:10px;top:10px;width:286px;height:174px}
.blog .date{position:absolute;left:14px;top:10px;width:40px;height:56px;background:#fff;text-align:center;font-size:10px;color:var(--navy);font-weight:600;line-height:1.3;padding-top:4px}
.blog .date b{display:block;background:var(--navy);color:#fff;font-size:10px;margin-top:4px;padding:2px 0}
.blog h4{position:absolute;left:16px;top:196px;width:280px;font-size:14px;font-weight:600;line-height:1.3}
.blog p{position:absolute;left:16px;top:238px;width:280px;font-size:10.5px;line-height:1.55;color:var(--muted)}
.blog a{position:absolute;left:16px;top:290px;font-size:12px;font-weight:500;color:var(--blue-bright)}

/* newsletter */
.news{left:0;top:4355px;width:1200px;height:209px;background:linear-gradient(90deg,#0a62b8,#1b8fd8 50%,#0a62b8)}

/* footer */
.footer{left:0;top:4564px;width:1200px;height:248px;background:var(--navy-deep);color:#fff}
.fcol{position:absolute;top:4596px}
.fcol h6{font-size:16px;font-weight:600;margin-bottom:10px}
.fcol li{list-style:none;font-size:10px;color:#c8c9dd;line-height:21px}
.fcol .row{display:flex;gap:10px;align-items:flex-start;font-size:10px;color:#c8c9dd;margin-bottom:12px;line-height:1.6}
.fcol .dot{width:20px;height:20px;border:1.5px solid #fff;border-radius:50%;flex:none}
.copy{position:absolute;left:0;width:1200px;top:4792px;text-align:center;font-size:10px;color:#c8c9dd}
.fline{position:absolute;left:120px;top:4782px;width:960px;height:1px;background:#3a3c72}
</style>
</head>
<body>

<div class="abs topbar">
  <span style="left:120px"><svg viewBox="0 0 12 12"><path d="M6 1a3.5 3.5 0 0 0-3.5 3.5C2.5 7.5 6 11 6 11s3.5-3.5 3.5-6.5A3.5 3.5 0 0 0 6 1z" fill="#fff"/></svg>PO Box 18, Marlow Vale, WA 6120</span>
  <span style="left:360px"><svg viewBox="0 0 12 12"><path d="M3 1l2 2-1 2a6 6 0 0 0 3 3l2-1 2 2-1.5 1.5C5 10 2 7 1.5 2.5z" fill="#fff"/></svg>1300 000 417</span>
  <span style="left:512px"><svg viewBox="0 0 12 12"><rect x="1" y="2.5" width="10" height="7" fill="#fff"/><path d="M1 2.5l5 4 5-4" stroke="#1f2062" fill="none"/></svg>hello@zerovanmedical.com</span>
  <span style="left:732px"><svg viewBox="0 0 12 12"><path d="M6 1a3.5 3.5 0 0 0-3.5 3.5C2.5 7.5 6 11 6 11s3.5-3.5 3.5-6.5A3.5 3.5 0 0 0 6 1z" fill="#fff"/></svg>Level 4 Harbour Court, 88 Quay Rd, Perth WA 6001</span>
</div>

<div class="abs nav">
  <div class="brand" style="left:110px;top:12px;font-size:20px"><i></i>Zerovan</div>
  <div class="links"><span class="on">Home</span><span>Services</span><span>Projects</span><span>Training</span><span>About</span></div>
  <div class="icon-round" style="left:816px"></div>
  <div class="icon-round" style="left:846px"></div>
  <div class="icon-round" style="left:876px"></div>
  <div class="btn" style="left:920px;top:12px;width:100px;height:28px;text-transform:none;font-size:12px">Contact Us</div>
  <div class="lang">En ⌄</div>
</div>

<div class="abs hero" role="img" aria-label="Pharmacist in a white coat standing between shelves of medical supplies"></div>
<div class="abs hero-text">
  <div class="welcome">Welcome To</div>
  <h1>Zerovan Medical</h1>
  <p>We are a medical supplier company we sell machines and equipment to all medical sectors in Iraq.</p>
</div>

<div class="abs quote"></div>
<div class="abs quote-tab">A request for Quote</div>
<div class="field" style="left:262px;top:533px;width:162px;height:28px">Name</div>
<div class="field" style="left:432px;top:533px;width:162px;height:28px">Email</div>
<div class="field" style="left:602px;top:533px;width:162px;height:28px">Phone Number</div>
<div class="field" style="left:770px;top:533px;width:168px;height:28px">Sub Category <span style="float:right">⌄</span></div>
<div class="field" style="left:262px;top:570px;width:676px;height:47px">Message</div>
<div class="btn" style="left:518px;top:632px;width:151px;height:32px">Submit</div>

<div class="section-title" style="top:705px">Our Services</div>
<div class="svc" style="left:120px">
  <svg class="ico" viewBox="0 0 74 74" fill="none" stroke="#1c1c1c" stroke-width="2.5"><circle cx="37" cy="30" r="22"/><circle cx="37" cy="30" r="10"/><rect x="12" y="56" width="50" height="10"/></svg>
  <h3>Medical Machines Supply</h3>
  <p>Common medical equipment may include oxygen equipment, wheelchairs, walkers, and crutches, while supplies could include replacement CPAP masks, nutritional formulas, support braces, diapers and catheter supplies.</p>
  <a>Read More</a>
</div>
<div class="svc" style="left:445px">
  <svg class="ico" viewBox="0 0 74 74" fill="none" stroke="#1c1c1c" stroke-width="2.5"><rect x="6" y="10" width="62" height="42"/><circle cx="30" cy="30" r="10"/><circle cx="48" cy="24" r="6"/><path d="M28 52v10M46 52v10M20 64h34"/></svg>
  <h3>Installation</h3>
  <p>Common medical equipment may include oxygen equipment, wheelchairs, walkers, and crutches, while supplies could include replacement CPAP masks, nutritional formulas, support braces, diapers and catheter supplies.</p>
  <a>Read More</a>
</div>
<div class="svc" style="left:770px">
  <svg class="ico" viewBox="0 0 74 74" fill="none" stroke="#1c1c1c" stroke-width="2.5"><rect x="30" y="6" width="38" height="26"/><circle cx="16" cy="16" r="7"/><circle cx="12" cy="52" r="6"/><circle cx="37" cy="52" r="6"/><circle cx="62" cy="52" r="6"/><path d="M4 70v-6h16v6M29 70v-6h16v6M54 70v-6h16v6"/></svg>
  <h3>Training the Staff</h3>
  <p>Common medical equipment may include oxygen equipment, wheelchairs, walkers, and crutches, while supplies could include replacement CPAP masks, nutritional formulas, support braces, diapers and catheter supplies.</p>
  <a>Read More</a>
</div>
<div class="btn" style="left:523px;top:1077px;width:150px;height:37px">View all services</div>

<div class="section-title" style="top:1146px">Product Catagory</div>
<div class="ph" style="left:120px;top:1209px;width:480px;height:481px;background:radial-gradient(ellipse 220px 160px at 240px 200px,#a9c9dc,rgba(169,201,220,0) 100%),linear-gradient(180deg,#e4eef5,#f2f6f9 70%,#e9eef2)" role="img" aria-label="Dental instruments laid out in a row"></div>
<div class="cat-label" style="left:120px;top:1585px;width:480px;text-align:center;font-size:21px">Dental Equipment</div>
<div class="outline-btn" style="left:303px;top:1622px;width:113px;height:38px">SHOP NOW</div>

<div class="ph" style="left:624px;top:1209px;width:451px;height:226px;background:radial-gradient(ellipse 140px 110px at 340px 110px,#9dbdd4,rgba(157,189,212,0) 100%),linear-gradient(90deg,#edf1f5 0%,#e2eaf1 50%,#c4d6e4 100%)" role="img" aria-label="Hospital monitoring and anaesthesia machines"></div>
<div class="cat-label" style="left:656px;top:1277px;font-size:21px;line-height:1.2">Hospital<br>Equipment</div>
<div class="outline-btn" style="left:656px;top:1336px;width:114px;height:38px">SHOP NOW</div>

<div class="ph" style="left:624px;top:1462px;width:451px;height:226px;background:radial-gradient(ellipse 70px 50px at 180px 190px,#e0454a,rgba(224,69,74,0) 100%),radial-gradient(ellipse 80px 90px at 90px 60px,#f3f5f8,rgba(243,245,248,0) 100%),linear-gradient(90deg,#6cc0ea,#49afe3)" role="img" aria-label="Laboratory flask and test tubes with red liquid"></div>
<div class="cat-label" style="left:880px;top:1522px;width:170px;text-align:center;font-size:21px;line-height:1.2;color:#fff">Laboratory<br>Equipment</div>
<div class="outline-btn" style="left:903px;top:1586px;width:114px;height:38px;border-color:#fff;color:#fff">SHOP NOW</div>

<div class="abs band"></div>
<div class="abs" style="left:127px;top:1791px;font-size:30px;font-weight:700">Our Products</div>
<div class="btn" style="left:918px;top:1792px;width:162px;height:38px">View all products</div>

<div class="prod" style="left:125px;top:1848px"><div class="img" style="background:radial-gradient(ellipse 90px 60px at 150px 80px,#3fc3d6,rgba(63,195,214,0) 100%),linear-gradient(160deg,#d9eef6,#a9cfe2)" role="img" aria-label="Blue examination shower chair"></div><h4>Quick Release Shower<br>Chair with Back</h4><div class="price">$67.00</div><div class="buy">SHOP NOW</div></div>
<div class="prod" style="left:450px;top:1848px"><div class="img" style="background:radial-gradient(ellipse 110px 40px at 150px 95px,#f4f6f8,rgba(244,246,248,0) 100%),linear-gradient(160deg,#c5d7e3,#8eaec4)" role="img" aria-label="Digital thermometer"></div><h4>Digital-Thermometer</h4><div class="price">$67.00</div><div class="buy">SHOP NOW</div></div>
<div class="prod" style="left:776px;top:1848px"><div class="img" style="background:radial-gradient(ellipse 80px 60px at 150px 85px,#5d6b7a,rgba(93,107,122,0) 100%),linear-gradient(160deg,#dcebf6,#9fc4e0)" role="img" aria-label="Blood glucose meter"></div><h4>Blood-Glucose-Meter</h4><div class="price">$67.00</div><div class="buy">SHOP NOW</div></div>
<div class="prod" style="left:125px;top:2177px"><div class="img" style="background:radial-gradient(ellipse 110px 60px at 140px 90px,#cfd5da,rgba(207,213,218,0) 100%),linear-gradient(160deg,#ffffff,#eef1f4)" role="img" aria-label="Stethoscope"></div><h4>Professional-Stethoscope</h4><div class="price">$18.99</div><div class="buy">SHOP NOW</div></div>
<div class="prod" style="left:450px;top:2177px"><div class="img" style="background:radial-gradient(ellipse 80px 70px at 147px 90px,#2c3e52,rgba(44,62,82,0) 100%),linear-gradient(160deg,#d2e7f5,#a3c9e6)" role="img" aria-label="Bathroom weighing scale with measuring tape"></div><h4>Weighting-Machine</h4><div class="price">$67.00</div><div class="buy">SHOP NOW</div></div>
<div class="prod" style="left:776px;top:2177px"><div class="img" style="background:radial-gradient(ellipse 40px 70px at 150px 130px,#3db86a,rgba(61,184,106,0) 100%),linear-gradient(160deg,#eaf3f9,#c3dcef)" role="img" aria-label="Green oxygen gas cylinder with regulator"></div><h4>Oxygen-Gas-Cylinder</h4><div class="price">$67.00</div><div class="buy">SHOP NOW</div></div>

<div class="ph" style="left:121px;top:2587px;width:451px;height:342px;background:var(--blue-bright)"></div>
<div class="ph" style="left:146px;top:2612px;width:401px;height:292px;background:radial-gradient(ellipse 120px 110px at 150px 140px,#3f9b8f,rgba(63,155,143,0) 100%),radial-gradient(ellipse 90px 60px at 260px 220px,#b99b73,rgba(185,155,115,0) 100%),linear-gradient(135deg,#dfe8ee,#9ab4c6)" role="img" aria-label="Staff in scrubs handling equipment deliveries"></div>
<div class="about">
  <h2>About Zerovan Medical</h2>
  <p>We are a medical supplier company we sell machines and equipment to all medical sectors in Iraq. Our services include not only the installation of these machines and equipment but also we provide support after installation and we train the staff to use these machines/equipment.</p>
</div>
<div class="btn" style="left:690px;top:2798px;width:119px;height:37px">Read More</div>

<div class="section-title" style="top:3012px">Our Customer Review</div>
<div class="arrow" style="left:131px">‹</div>
<div class="arrow" style="left:1131px">›</div>
<div class="rev" style="left:163px"><div class="top"><div class="q">“</div><p>EWhen you lack good health, everything else in life suffers. It's harder toconcentrate and study. Illness can couse you to fall behind in coursework. Stress can make you feel overwhelmed.</p></div><div class="avatar"><i></i></div><h5>Sam Ardent</h5><div class="stars">★★★★★</div></div>
<div class="rev" style="left:488px"><div class="top"><div class="q">“</div><p>EWhen you lack good health, everything else in life suffers. It's harder toconcentrate and study. Illness can couse you to fall behind in coursework. Stress can make you feel overwhelmed.</p></div><div class="avatar"><i></i></div><h5>Sam Ardent</h5><div class="stars">★★★★★</div></div>
<div class="rev" style="left:813px"><div class="top"><div class="q">“</div><p>EWhen you lack good health, everything else in life suffers. It's harder toconcentrate and study. Illness can couse you to fall behind in coursework. Stress can make you feel overwhelmed.</p></div><div class="avatar"><i></i></div><h5>Sam Ardent</h5><div class="stars">★★★★★</div></div>

<div class="abs train" role="img" aria-label="Technician in protective gear operating factory machinery"></div>
<h2 class="abs" style="left:120px;top:3555px;font-size:31px;font-weight:700;line-height:1.25;color:#17184a">We Training the staff<br>to use these machines</h2>
<div class="play"><svg viewBox="0 0 50 50" style="width:50px;height:50px"><circle cx="25" cy="25" r="17" fill="#1b8fd8"/><path d="M21 17l11 8-11 8z" fill="#fff"/></svg></div>
<div class="watch">Watch video</div>

<div class="section-title" style="top:3866px">Latest Blog</div>
<div class="blog" style="left:120px"><div class="img" style="background:radial-gradient(ellipse 60px 40px at 230px 30px,#f0522e,rgba(240,82,46,0) 100%),radial-gradient(ellipse 70px 60px at 150px 110px,#4aa0d8,rgba(74,160,216,0) 100%),linear-gradient(150deg,#f1f3f5,#d9e2ea)" role="img" aria-label="Hands using a tablet beside lab samples"></div><div class="date">3<br>April<b>2024</b></div><h4>Lorem ipsum dolor sit amet, consectetur adipiscing elit.</h4><p>Lorem ipsum dolor sit amet, consectetur adipiscing elit. Suspendisse sed urna nec orci hendrerit eleifend sit amet ut ligula.</p><a>Read More →</a></div>
<div class="blog" style="left:445px"><div class="img" style="background:radial-gradient(ellipse 80px 40px at 160px 40px,#d6b98c,rgba(214,185,140,0) 100%),radial-gradient(ellipse 90px 50px at 150px 120px,#8fb8dc,rgba(143,184,220,0) 100%),linear-gradient(150deg,#eef2f6,#c6d6e4)" role="img" aria-label="Delivery truck with medical supply boxes"></div><div class="date">3<br>April<b>2024</b></div><h4>Lorem ipsum dolor sit amet, consectetur adipiscing elit.</h4><p>Lorem ipsum dolor sit amet, consectetur adipiscing elit. Suspendisse sed urna nec orci hendrerit eleifend sit amet ut ligula.</p><a>Read More →</a></div>
<div class="blog" style="left:770px"><div class="img" style="background:radial-gradient(ellipse 100px 60px at 170px 120px,#5a88c2,rgba(90,136,194,0) 100%),linear-gradient(150deg,#dbe7f2,#94b4d2)" role="img" aria-label="Laboratory worker typing on a laptop"></div><div class="date">3<br>April<b>2024</b></div><h4>Lorem ipsum dolor sit amet, consectetur adipiscing elit.</h4><p>Lorem ipsum dolor sit amet, consectetur adipiscing elit. Suspendisse sed urna nec orci hendrerit eleifend sit amet ut ligula.</p><a>Read More →</a></div>
<div class="btn navy" style="left:536px;top:4271px;width:126px;height:37px">View all blog</div>

<div class="abs news"></div>
<h2 class="abs" style="left:0;width:1200px;top:4396px;text-align:center;color:#fff;font-size:31px;font-weight:700">Subscribe For Newsletter</h2>
<p class="abs" style="left:0;width:1200px;top:4440px;text-align:center;color:#fff;font-size:11px">Subscribe for newsletter and get our daily updates right to you inbox</p>
<div class="abs" style="left:338px;top:4463px;width:522px;height:43px;background:#fff;font-size:12px;color:#555;padding:13px 22px">Enter Your Email</div>
<div class="btn navy" style="left:742px;top:4468px;width:112px;height:33px">Subscribe</div>

<div class="abs footer"></div>
<div class="fcol" style="left:122px">
  <div class="brand" style="position:static;color:#fff;font-size:20px"><i style="border-color:#fff"></i>Zerovan</div>
  <p style="font-size:10px;color:#c8c9dd;line-height:1.6;width:210px;margin-top:22px">We are a medical supplier company we sell machines and equipment to all medical sectors in Iraq.</p>
</div>
<div class="fcol" style="left:459px"><h6>Quick links</h6><ul><li>Home</li><li>Projects</li><li>Services</li><li>Projects</li><li>Training</li><li>About</li><li>Contact us</li></ul></div>
<div class="fcol" style="left:682px"><h6>Contact Us</h6>
  <div class="row"><span class="dot"></span>1300 000 417</div>
  <div class="row"><span class="dot"></span>hello@zerovanmedical.com</div>
  <div class="row"><span class="dot"></span>Level 4 Harbour Court,<br>88 Quay Rd, Perth WA 6001</div>
</div>
<div class="fcol" style="left:991px"><h6>Follow us</h6>
  <div class="row"><span class="dot"></span>Newsfeed</div>
  <div class="row"><span class="dot"></span>Photostream</div>
</div>
<div class="fline"></div>
<div class="copy">Copyright © 2024, Zerovan Medical All rights reserved.</div>

</body>
</html>
```